UI Design & Web Design for Used Car Dealer.
Modern and user friendly responsive layout for mobiles and desktop. Bootstrap and form elements for members,registration process,login,dashboard. Layouts for Home Page, Car Listing Pages, Individual Car Information page and etc.

Output files in Bootstrap Html/CSS
Please refer to attachments for more details.

Target Market(s)

Asia / Singapore

Industry/Entity Type

Car Dealer

Coding

Coded - Design and coding required

Number of Pages Required

5+ page

Font styles to use
Sans Serif

Colors
acd037
f6faec
cfcfcf
b1b1b1
ffffff

Requirements
Must have
• Coded in Bootstrap 3 UI Elements, Forms, Labels, Sections, Tables, Buttons, Alerts, Modal, Fonts, Dashboard, Login, Register,Contact
Nice to have
• Stock Images
Should not have
• NA

```html
<!DOCTYPE html>
<html lang="en">
<head>
<meta charset="utf-8">
<title>Drivenest – Home</title>
<link href="https://fonts.googleapis.com/css2?family=Saira:wght@300;400;500;600&display=swap" rel="stylesheet">
<style>
  :root {
    --green: #6cbf3a;
    --green-line: #acd037;
    --white: #ffffff;
    --ink: #4a4a4a;
    --muted: #7a7a7a;
    --rule: #cfcfcf;
    --section-bg: #f4f4f4;
    --footer-bg: #2f2f2f;
    --footer-text: #a9a9a9;
  }
  * { margin: 0; padding: 0; box-sizing: border-box; }
  html, body { width: 1200px; height: 1200px; overflow: hidden; }
  body {
    font-family: "Saira", sans-serif;
    background: var(--white);
    position: relative;
  }

  /* Hero */
  .hero {
    position: absolute; left: 0; top: 0; width: 1200px; height: 630px;
    overflow: hidden;
  }
  .hero-photo {
    position: absolute; inset: 0;
    background:
      radial-gradient(ellipse 360px 150px at 760px 290px, rgba(210,50,25,0.95), rgba(150,30,15,0.6) 55%, rgba(0,0,0,0) 100%),
      radial-gradient(ellipse 300px 200px at 300px 250px, rgba(150,90,50,0.35), rgba(0,0,0,0) 100%),
      linear-gradient(180deg, #2a3530 0%, #3a4640 35%, #24302a 60%, #0d120f 100%);
  }
  .hero-shade {
    position: absolute; left: 0; right: 0; bottom: 0; height: 260px;
    background: linear-gradient(180deg, rgba(0,0,0,0) 0%, rgba(0,0,0,0.55) 100%);
  }
  .brand {
    position: absolute; left: 186px; top: 43px;
    display: flex; align-items: center; gap: 10px;
  }
  .brand-mark { width: 40px; height: 31px; background: var(--green); border-radius: 3px; }
  .brand-name { color: var(--green); font-size: 24px; font-weight: 500; letter-spacing: 1px; }
  .main-nav {
    position: absolute; top: 48px; right: 180px;
    display: flex; gap: 23px; list-style: none;
  }
  .main-nav li { color: var(--white); font-size: 11.5px; font-weight: 400; letter-spacing: -0.2px; }
  .main-nav li.is-active { color: var(--green); font-weight: 600; font-size: 13px; margin-top: -1px; }

  .hero-copy { position: absolute; left: 188px; top: 424px; width: 830px; }
  .hero-title {
    color: var(--white); font-weight: 400; font-size: 50px; line-height: 1.1;
    letter-spacing: -1px; display: inline-block;
    padding-bottom: 6px; border-bottom: 1px solid var(--green);
  }
  .hero-text {
    margin-top: 14px; color: var(--white); font-size: 17.5px; font-weight: 300;
    line-height: 23px; letter-spacing: -0.1px;
  }

  /* Intro section */
  .features {
    position: absolute; left: 0; top: 630px; width: 1200px; height: 496px;
    background: linear-gradient(180deg, #e6e6e6 0%, var(--section-bg) 12%, var(--white) 100%);
    overflow: hidden;
  }
  .feature-photo {
    position: absolute; right: 0; top: 150px; width: 240px; height: 346px;
    background:
      radial-gradient(ellipse 140px 190px at 170px 190px, #f2f2f2 0%, #d9d9d9 55%, rgba(255,255,255,0) 100%),
      radial-gradient(ellipse 120px 80px at 190px 110px, #5a5a5a 0%, rgba(90,90,90,0) 100%);
  }
  .intro { position: absolute; left: 188px; top: 60px; }
  .intro-kicker { color: var(--muted); font-size: 20px; font-weight: 300; }
  .intro-title { color: var(--green); font-size: 57px; font-weight: 400; line-height: 1; margin-top: 8px; letter-spacing: -1px; }
  .intro-sub { color: var(--muted); font-size: 15.5px; font-weight: 300; margin-top: 10px; }
  .section-rule { position: absolute; left: 188px; top: 224px; width: 832px; height: 1px; background: var(--rule); }

  .feature-list { position: absolute; left: 189px; top: 275px; display: flex; }
  .feature-card { width: 299px; }
  .feature-title { color: var(--ink); font-size: 19px; font-weight: 400; letter-spacing: -0.3px; }
  .feature-rule { width: 78px; height: 2px; background: var(--green); margin-top: 3px; }
  .feature-text {
    color: var(--muted); font-size: 11.5px; font-weight: 300; line-height: 16px;
    margin-top: 11px; width: 230px;
  }
  .btn-read {
    display: inline-block; margin-top: 21px; background: var(--green); color: var(--white);
    font-size: 9.5px; font-weight: 600; padding: 5px 10px; border-radius: 2px; letter-spacing: 0.2px;
  }

  /* Footer */
  .site-footer {
    position: absolute; left: 0; top: 1126px; width: 1200px; height: 74px;
    background: var(--footer-bg); color: var(--footer-text); font-size: 10px; font-weight: 300;
  }
  .footer-links { position: absolute; left: 120px; top: 30px; }
  .copyright { position: absolute; right: 106px; top: 30px; }
</style>
</head>
<body>
  <header class="hero">
    <div class="hero-photo" role="img" aria-label="Red sports car parked at night under a concrete overpass on wet asphalt"></div>
    <div class="hero-shade"></div>
    <div class="brand">
      <span class="brand-mark"></span>
      <span class="brand-name">DRIVENEST</span>
    </div>
    <ul class="main-nav">
      <li class="is-active">HOME</li>
      <li>BENEFITS</li>
      <li>VEHICLE LISTINGS</li>
      <li>START ADVERTISING NOW</li>
      <li>CONTACT</li>
    </ul>
    <div class="hero-copy">
      <h1 class="hero-title">WE’VE GOT IT ARRANGED</h1>
      <p class="hero-text">Drivenest.com is an online platform which covers every single aspects from buying to selling of your vehicles. From engagement of a Servicing Agent till successfully handing over its ownership through a smarter and secure solutions</p>
    </div>
  </header>

  <section class="features">
    <div class="feature-photo" role="img" aria-label="White sports car in soft misty light"></div>
    <div class="intro">
      <p class="intro-kicker">With Drivenest.com platform</p>
      <h2 class="intro-title">THE MARGIN IS YOURS</h2>
      <p class="intro-sub">when you reaches out to potential vehicle enthusiasts directly.</p>
    </div>
    <div class="section-rule"></div>
    <div class="feature-list">
      <article class="feature-card">
        <h3 class="feature-title">ADVERTISE NOW</h3>
        <div class="feature-rule"></div>
        <p class="feature-text">Upload images and vehicle details right after creating an account which is absolutely hassle &amp; cost free.</p>
        <span class="btn-read">READ MORE</span>
      </article>
      <article class="feature-card">
        <h3 class="feature-title">PROMOTE YOUR BUSINESS</h3>
        <div class="feature-rule"></div>
        <p class="feature-text">Leverage our busy online traffic which makes us an excellent business platform for limitless exposure.</p>
        <span class="btn-read">READ MORE</span>
      </article>
      <article class="feature-card">
        <h3 class="feature-title">ONLINE INSURANCE</h3>
        <div class="feature-rule"></div>
        <p class="feature-text">Fill up your details on one form, we will provide several quotation to suits your requirement.</p>
        <span class="btn-read">READ MORE</span>
      </article>
    </div>
  </section>

  <footer class="site-footer">
    <div class="footer-links">Home &nbsp;|&nbsp; Privacy &nbsp;|&nbsp; Terms and Conditions &nbsp;|&nbsp; Contact us</div>
    <div class="copyright">Copyright © 2016. All Right Reserved</div>
  </footer>
</body>
</html>
```